Redesign cement bags for leading cement producer in south east asia

We are from Larkfield cement and would like to redesign our bag to relaunch the product line. Our bags are made of high quality PP woven sack. We are one of the leading cement producers and we want our bags to have a Larkfield classy look on each visible side when it is loading in a truck or stacking on a pallet.

Thank you for interesting in this project. Good luck.

Project Deadline Extended Reason: Hi all, I have received requests to extend the deadline. Some of the work requires revising and some of them are still on process. To be fair, I also raise my budget to compensate the time. Thanks all for your participation. Added Sunday, July 10, 2016

Target Market(s)

Construction

Industry/Entity Type

Cement

Requirements
Must have
• You will have to design two bags for two cement grades. 52.5 is of higher grade and 42.5 is of lower grade. Both are similar in design but a distinctive colours to differentiate the two at once. Please look at Reference picture 2 for ideas.
Nice to have
• You do not have to change the original logo but the Larkfield cement word font changes are required. There are no restrictions to colours and font but please refrain from using feminine colours. Instructions on rear side of the bags are now included in the scope. Please create new layout and design new user friendly symbols.
Should not have
• Since cement is a dusty product, you need avoid some colours like black as background. The dust need to be less obvious to attract attention. Our previous base colour are shown in below.
• We want a fresh look on our bag, please do not just copy our old design and make small changes. I have attached our competitors' design, please refrain from using their design as well.
• It is recommend to do some research on cement bag sector.

```html
<!DOCTYPE html>
<html lang="en">
<head>
<meta charset="utf-8">
<title>Larkfield Cement – Bag Range</title>
<link rel="stylesheet" href="https://fonts.googleapis.com/css2?family=Anton&family=Archivo:wght@700&family=Mulish:wght@300;400&display=swap">
<style>
  :root{
    --page:#ffffff;
    --sack:#ececec;
    --band:#d2d2d2;
    --premium:#0b3aa8;
    --premium-soft:#c7d2ec;
    --standard:#d98a12;
    --standard-soft:#f2dcb8;
  }
  *{margin:0;padding:0;box-sizing:border-box}
  html,body{width:1200px;height:1200px;overflow:hidden;background:var(--page)}
  .canvas{position:relative;width:1200px;height:1200px}

  .bag{position:absolute;background:var(--sack);overflow:hidden}
  .bag--premium{--ink:var(--premium);--ink-soft:var(--premium-soft)}
  .bag--standard{--ink:var(--standard);--ink-soft:var(--standard-soft)}
  .front{width:432px;height:688px}
  .front--premium{left:52px;top:240px}
  .front--standard{left:724px;top:304px}
  .gusset{left:532px;top:248px;width:148px;height:672px}

  .band{position:absolute;left:120px;top:0;width:172px;height:100%;background:var(--band);opacity:.75}

  .brand-mark{position:absolute;left:0;width:100%;display:flex;align-items:center;justify-content:center;gap:12px;
    font-family:"Archivo",sans-serif;font-weight:700;color:var(--ink);font-size:26px;letter-spacing:1px}
  .brand-mark__dot{width:22px;height:22px;border-radius:50%;background:var(--ink)}
  .front .brand-mark{top:100px}

  .wordmark{position:absolute;left:0;top:0;width:100%;height:100%;font-family:"Anton",sans-serif;
    color:var(--ink);text-transform:uppercase;line-height:1;font-weight:400}
  .wordmark__name,.wordmark__type{position:absolute;left:0;width:100%;text-align:center;display:block;white-space:nowrap}
  .wordmark__name{top:196px;font-size:66px;letter-spacing:1px}
  .wordmark__type{top:272px;font-size:62px;letter-spacing:1px}

  .spec{position:absolute;left:0;top:0;width:100%;height:100%;color:var(--ink)}
  .spec__line{position:absolute;left:0;width:100%;text-align:center;font-family:"Mulish",sans-serif;font-weight:400;line-height:1.2;white-space:nowrap}
  .spec__range{top:352px;font-family:"Archivo",sans-serif;font-weight:700;font-size:20px}
  .spec__grade{top:384px;font-size:28px}
  .spec__quality{top:416px;font-size:21px}
  .spec__weight{top:446px;font-size:38px;font-weight:300}
  .spec__net{top:490px;font-size:21px}

  .pattern{position:absolute;left:0;bottom:0;width:100%;
    background:linear-gradient(180deg,var(--ink-soft) 0%,var(--ink) 140%)}
  .front .pattern{top:530px}
  .gusset .pattern{top:500px}

  .gusset .brand-mark{top:70px;font-size:0}
  .gusset .brand-mark__dot{width:40px;height:40px}
  .gusset__label{position:absolute;left:-92px;top:254px;width:340px;height:100px;transform:rotate(-90deg);
    display:flex;flex-direction:column;justify-content:center;color:var(--ink)}
  .gusset__name{font-family:"Anton",sans-serif;font-size:42px;line-height:1;text-transform:uppercase;white-space:nowrap}
  .gusset__spec{font-family:"Mulish",sans-serif;font-size:20px;margin-top:6px;white-space:nowrap;letter-spacing:.5px}
  .gusset__spec b{font-family:"Archivo",sans-serif}
</style>
</head>
<body>
<main class="canvas">

  <section class="bag bag--premium front front--premium" aria-label="Grade 52.5 bag front">
    <div class="band"></div>
    <div class="brand-mark"><span class="brand-mark__dot"></span>Larkfield</div>
    <h1 class="wordmark"><span class="wordmark__name">Larkfield</span><span class="wordmark__type">Cement</span></h1>
    <div class="spec">
      <p class="spec__line spec__range">PORTLAND</p>
      <p class="spec__line spec__grade">52.5</p>
      <p class="spec__line spec__quality">Export Quality</p>
      <p class="spec__line spec__weight">50Kg</p>
      <p class="spec__line spec__net">Net Weight</p>
    </div>
    <div class="pattern" role="img" aria-label="Repeating brand motif pattern in blue"></div>
  </section>

  <section class="bag bag--premium gusset" aria-label="Grade 52.5 bag side">
    <div class="brand-mark"><span class="brand-mark__dot"></span>Larkfield</div>
    <div class="gusset__label">
      <p class="gusset__name">Larkfield Cement</p>
      <p class="gusset__spec">Class <b>52.5</b>&nbsp;&nbsp;NET WEIGHT <b>50Kg</b></p>
    </div>
    <div class="pattern" role="img" aria-label="Repeating brand motif pattern in blue"></div>
  </section>

  <section class="bag bag--standard front front--standard" aria-label="Grade 42.5 bag front">
    <div class="band"></div>
    <div class="brand-mark"><span class="brand-mark__dot"></span>Larkfield</div>
    <h2 class="wordmark"><span class="wordmark__name">Larkfield</span><span class="wordmark__type">Cement</span></h2>
    <div class="spec">
      <p class="spec__line spec__range">PORTLAND</p>
      <p class="spec__line spec__grade">42.5</p>
      <p class="spec__line spec__quality">Export Quality</p>
      <p class="spec__line spec__weight">50Kg</p>
      <p class="spec__line spec__net">Net Weight</p>
    </div>
    <div class="pattern" role="img" aria-label="Repeating brand motif pattern in orange"></div>
  </section>

</main>
</body>
</html>
```